Riverpeak Analytics needs new design business card

We are video surveillance and analytics software development company.
I am looking for a professional business card.
Our website is www.riverpeakanalytics.example.au
Please have a loo and get the feel for who we are and what we do.
I do not know what else to give you apart from good luck and I hope your design gets selected.
Thank you very much for participating
Business
Contact Information for Business Card
Address
27/15 Marlowe Street Fernbrook NSW 2199
Telephone 1300 582 417
Mobile 0450 731 258
email: marcus@riverpeakanalytics.example.au
name
Marcus Helvard
Position
Managing Director
Font styles to use
Other font styles liked:
- Arial
Look and feel

```html
<!DOCTYPE html>
<html lang="en">
<head>
<meta charset="utf-8">
<title>Riverpeak Analytics – Business Card</title>
<link href="https://fonts.googleapis.com/css2?family=Arimo:wght@400;700&display=swap" rel="stylesheet">
<style>
  :root {
    --navy: #1d3f6e;
    --navy-deep: #14305a;
    --steel: #8a9aae;
    --ink: #3b4f6e;
    --grey: #7b8594;
    --paper: #ffffff;
    --paper-shade: #eef0f3;
    --backdrop: #e6e3de;
  }
  * { margin: 0; padding: 0; box-sizing: border-box; }
  html, body { width: 1200px; height: 1023px; overflow: hidden; }
  body {
    background: var(--backdrop);
    font-family: "Arimo", Arial, sans-serif;
    position: relative;
  }
  .card {
    position: absolute;
    left: 250px;
    width: 700px;
    height: 400px;
    box-shadow: 0 6px 18px rgba(0,0,0,0.18);
    overflow: hidden;
  }
  /* Front */
  .card-front {
    top: 80px;
    background: linear-gradient(180deg, var(--paper) 0%, var(--paper-shade) 100%);
  }
  .front-brand {
    position: absolute;
    left: 60px; top: 136px;
    width: 250px;
    display: flex; align-items: center; gap: 14px;
  }
  .brand-square {
    width: 34px; height: 34px;
    background: var(--navy);
    flex: none;
  }
  .brand-name {
    font-weight: 700;
    font-size: 27px;
    line-height: 30px;
    color: var(--navy);
    letter-spacing: 0.5px;
  }
  .front-brand .brand-name { display: flex; flex-direction: column; }
  .divider {
    position: absolute;
    left: 345px; top: 60px;
    width: 1px; height: 220px;
    background: linear-gradient(180deg, transparent, var(--steel), transparent);
  }
  .person {
    position: absolute;
    left: 370px; top: 62px;
  }
  .person-name {
    font-size: 26px;
    color: var(--ink);
    font-weight: 400;
  }
  .person-title {
    font-size: 14px;
    color: var(--grey);
    margin-top: 4px;
  }
  .contact {
    position: absolute;
    left: 370px; top: 140px;
    list-style: none;
    font-size: 14px;
    color: var(--ink);
    line-height: 22px;
  }
  .contact li { display: flex; align-items: flex-start; gap: 8px; }
  .contact svg { width: 14px; height: 14px; margin-top: 4px; flex: none; fill: var(--ink); }
  .contact .address { margin-bottom: 2px; }
  .bar-band {
    position: absolute;
    left: 0; right: 0; bottom: 0;
    height: 70px;
    background: linear-gradient(180deg, rgba(29,63,110,0) 0%, rgba(29,63,110,0.45) 55%, var(--navy) 100%);
  }
  /* Back */
  .card-back {
    top: 540px;
    border-radius: 22px;
    background: linear-gradient(150deg, #2f5688 0%, var(--navy) 45%, var(--navy-deep) 100%);
  }
  .back-brand {
    position: absolute;
    left: 0; right: 0; top: 170px;
    display: flex; justify-content: center; align-items: center; gap: 16px;
  }
  .back-brand .brand-square { background: var(--paper); width: 40px; height: 40px; }
  .back-brand .brand-name { color: var(--paper); font-size: 36px; line-height: 40px; }
  .back-web {
    position: absolute;
    left: 40px; right: 40px; bottom: 34px;
    display: flex; align-items: center; gap: 14px;
    color: #c9d4e3;
    font-size: 14px;
    letter-spacing: 0.5px;
  }
  .back-web .rule { flex: 1; height: 1px; background: #9fb2cb; }
</style>
</head>
<body>
  <section class="card card-front">
    <div class="front-brand">
      <span class="brand-square"></span>
      <span class="brand-name"><span>Riverpeak</span><span>Analytics</span></span>
    </div>
    <div class="divider"></div>
    <div class="person">
      <p class="person-name">Marcus Helvard</p>
      <p class="person-title">Managing Director</p>
    </div>
    <ul class="contact">
      <li class="address"><span>27/15 Marlowe Street<br>Fernbrook NSW 2199</span></li>
      <li><svg viewBox="0 0 14 14"><rect x="1" y="5" width="12" height="8" rx="1"/><rect x="3" y="1" width="8" height="3"/></svg><span>1300 582 417</span></li>
      <li><svg viewBox="0 0 14 14"><rect x="4" y="0" width="6" height="14" rx="1"/></svg><span>0450 731 258</span></li>
      <li><svg viewBox="0 0 14 14"><path d="M1 3h12v8H1z M1 3l6 5 6-5" fill="none" stroke="#3b4f6e" stroke-width="1.4"/></svg><span>marcus@riverpeakanalytics.example.au</span></li>
      <li><svg viewBox="0 0 14 14"><rect x="1" y="1" width="12" height="9" fill="none" stroke="#3b4f6e" stroke-width="1.4"/><rect x="5" y="11" width="4" height="2"/></svg><span>www.riverpeakanalytics.example.au</span></li>
    </ul>
    <div class="bar-band" role="img" aria-label="Decorative band of rising blue bars along the lower edge"></div>
  </section>

  <section class="card card-back">
    <div class="back-brand">
      <span class="brand-square"></span>
      <span class="brand-name">Riverpeak Analytics</span>
    </div>
    <div class="back-web">
      <span>www.riverpeakanalytics.example.au</span>
      <span class="rule"></span>
    </div>
  </section>
</body>
</html>
```